Promo Flyer to put in prize bags at carnival

I am owner of Willow & Pike Hair Salon located in Gahanna, OH. I’m sponsoring a community carnival when I will be putting flyers in all attendees prize bags. This flyer will communicate details of my salon on one side (picture of me, logo, description of business, address, website, email, phone #) and the other side will showcase and a 50% discount for first time customers. Flyer can be 5” x 7” or greater

Side 1 details:
-Logo will be attached to this brief
-picture of me will be attached to this brief
-address: 2641 W. Brockton Ave, Suite 17, Brierfield, OH, 43299
-website: wphairstudio.example
-email: Dorian.blake@wphairstudio.example
-phone: 614-55-GOWPS (46977)

Side 2 details:
-‘Guess what? You get 50% off your 1st service at Willow & Pike Hair Salon.’
-‘Expires 7/31/2018’
-Hair | Fashion | Photography
-Visit wphairstudio.example to book your service
-must present this flyer at time of service to receive discount

Industry/Entity Type

Hair And Beauty

Font styles to use
Other font styles liked:
• Inoxida

Colors
3176b5
000000
ffffff

Requirements
Must have
• 2 sides
• Color scheme to match logo

```html
<!DOCTYPE html>
<html lang="en">
<head>
<meta charset="utf-8">
<title>Willow &amp; Pike Hair Salon – Carnival Flyer</title>
<link rel="stylesheet" href="https://fonts.googleapis.com/css2?family=Archivo+Black&family=Great+Vibes&family=Lobster&family=Oswald:wght@500;700&display=swap">
<style>
  :root {
    --blue: #3f82cc;
    --blue-deep: #3176b5;
    --gold: #f2b225;
    --gold-light: #fbe3a1;
    --black: #0f0f10;
    --white: #ffffff;
    --photo-dark: #3a4650;
    --photo-mid: #7b8894;
  }
  * { margin: 0; padding: 0; box-sizing: border-box; }
  html, body { width: 1200px; height: 993px; overflow: hidden; background: var(--white); }
  .canvas { position: relative; width: 1200px; height: 993px; }

  .flyer {
    position: absolute; width: 490px; height: 690px; overflow: hidden;
    box-shadow: 0 6px 18px rgba(0,0,0,.25); background: var(--black);
  }
  .flyer--info { left: 60px; top: 64px; }
  .flyer--promo { left: 640px; top: 230px; }

  .abs { position: absolute; }

  /* Info side */
  .top-strip { left: 0; top: 0; width: 490px; height: 22px; background: var(--blue); }
  .brand-mark { left: 221px; top: 76px; width: 48px; height: 48px; border-radius: 50%; background: var(--gold); }
  .brand-name {
    left: 0; top: 176px; width: 490px; text-align: center;
    font-family: "Great Vibes", cursive; font-size: 68px; color: var(--white); line-height: 1;
  }
  .portrait { left: 0; top: 312px; width: 262px; height: 378px;
    background: linear-gradient(160deg, var(--photo-mid), var(--photo-dark) 60%, #23303a); }
  .satin { left: 262px; top: 360px; width: 228px; height: 280px;
    background: linear-gradient(135deg, var(--gold) 0%, var(--gold-light) 35%, var(--gold) 60%, #fff4d6 85%, var(--gold) 100%); }
  .contact-bar { left: 262px; top: 312px; width: 228px; height: 48px; background: var(--black);
    font-family: "Oswald", sans-serif; font-weight: 700; font-size: 30px; color: var(--white);
    padding-left: 40px; line-height: 48px; }
  .base-strip { left: 262px; top: 640px; width: 228px; height: 50px; background: var(--blue); }
  .contact-list { left: 272px; top: 376px; width: 210px; font-family: "Oswald", sans-serif; font-weight: 700; color: var(--black); }
  .contact-item { font-size: 12px; margin-bottom: 20px; line-height: 1.3; white-space: nowrap; }
  .contact-item--web { font-size: 16px; }
  .contact-item--phone { display: flex; align-items: center; gap: 8px; font-size: 14px; margin-top: 28px; }
  .contact-item--addr { text-align: center; font-size: 13.5px; margin-top: -4px; white-space: normal; }
  .pin { display: block; margin: 0 auto 12px; }

  /* Promo side */
  .services-bar { left: 0; top: 0; width: 490px; height: 84px; background: var(--blue);
    font-family: "Archivo Black", sans-serif; font-size: 28px; color: var(--black);
    text-align: center; line-height: 96px; white-space: nowrap; }
  .teaser-strip { left: 0; top: 84px; width: 490px; height: 108px;
    background: linear-gradient(100deg, var(--gold) 0%, #fde9b0 40%, var(--gold) 75%); }
  .teaser-photo { left: 330px; top: 84px; width: 160px; height: 108px;
    background: linear-gradient(135deg, #6b5546, #2b211c); }
  .teaser { left: 38px; top: 100px; font-family: "Lobster", cursive; font-size: 50px; color: var(--black); }
  .offer { left: 0; top: 222px; width: 490px; text-align: center; color: var(--white);
    font-family: "Oswald", sans-serif; font-weight: 700; }
  .offer-main { font-size: 42px; line-height: 1.05; }
  .offer-sub { font-size: 26px; line-height: 1.2; }
  .offer-name { font-family: "Great Vibes", cursive; font-weight: 400; font-size: 70px; line-height: 1.1; }
  .expiry { right: 34px; top: 420px; font-family: "Oswald", sans-serif; font-weight: 500; font-size: 19px; color: var(--white); }
  .booking-area { left: 0; top: 470px; width: 490px; height: 172px;
    background: linear-gradient(120deg, #fff6df 0%, var(--gold) 45%, #fff 70%, var(--gold-light) 100%); }
  .booking-photo { left: 0; top: 470px; width: 220px; height: 172px;
    background: linear-gradient(150deg, #8c9aa6, #3a2c25 70%); }
  .booking { left: 220px; top: 508px; width: 270px; text-align: center; font-family: "Oswald", sans-serif; font-weight: 700; }
  .booking-visit { color: var(--blue-deep); font-size: 17px; }
  .booking-site { color: var(--black); font-size: 20px; }
  .booking-tail { color: var(--blue-deep); font-size: 17px; }
  .terms-bar { left: 0; top: 642px; width: 490px; height: 48px; background: var(--blue);
    font-family: "Oswald", sans-serif; font-weight: 500; font-size: 15px; color: var(--white);
    text-align: center; line-height: 48px; white-space: nowrap; }
</style>
</head>
<body>
<div class="canvas">

  <section class="flyer flyer--info">
    <div class="abs top-strip"></div>
    <div class="abs brand-mark"></div>
    <div class="abs brand-name">Willow &amp; Pike</div>
    <div class="abs portrait" role="img" aria-label="Portrait photo of the salon owner in a blue suit"></div>
    <div class="abs satin" role="img" aria-label="Gold satin fabric background"></div>
    <div class="abs contact-bar">Contact:</div>
    <div class="abs base-strip"></div>
    <div class="abs contact-list">
      <div class="contact-item">Dorian.blake@wphairstudio.example</div>
      <div class="contact-item contact-item--web">wphairstudio.example</div>
      <div class="contact-item contact-item--phone">
        <svg width="12" height="18" viewBox="0 0 12 18" aria-hidden="true"><path d="M3 1 L6 1 L6 5 L4 6 Q4 11 7 13 L9 11 L11 13 L10 17 Q2 16 1 6 Z" fill="#0f0f10"/></svg>
        614-55-GOWPS (46977)
      </div>
      <div class="contact-item contact-item--addr">
        <svg class="pin" width="16" height="22" viewBox="0 0 16 22" aria-hidden="true"><path d="M8 1 A7 7 0 0 1 15 8 C15 13 8 21 8 21 C8 21 1 13 1 8 A7 7 0 0 1 8 1 Z" fill="none" stroke="#0f0f10" stroke-width="2"/><circle cx="8" cy="8" r="2.5" fill="#0f0f10"/></svg>
        2641 W. Brockton Ave, Suite 17,<br>Brierfield, OH, 43299
      </div>
    </div>
  </section>

  <section class="flyer flyer--promo">
    <div class="abs services-bar">Hair | Fashion | Photography</div>
    <div class="abs teaser-strip"></div>
    <div class="abs teaser-photo" role="img" aria-label="Photo of braided hairstyle seen from behind"></div>
    <div class="abs teaser">Guess What ?</div>
    <div class="abs offer">
      <div class="offer-main">You get 50% off</div>
      <div class="offer-sub">your 1st service at</div>
      <div class="offer-name">Willow &amp; Pike</div>
    </div>
    <div class="abs expiry">Expires 7/31/2018</div>
    <div class="abs booking-area"></div>
    <div class="abs booking-photo" role="img" aria-label="Photo of a fade haircut with a shaved line design"></div>
    <div class="abs booking">
      <div class="booking-visit">Visit</div>
      <div class="booking-site">wphairstudio.example</div>
      <div class="booking-tail">to book your service</div>
    </div>
    <div class="abs terms-bar">Must present this flyer at time of service to receive discount</div>
  </section>

</div>
</body>
</html>
```